Electrical company business card design.

Hi, were an electrical company in Ravenmoor New Zealand called Quarneth Ltd. We focus mainly on high end residential and commercial so the card would be targeted towards that.
The card will be for myself, i am the director of the company.
Name: Derek Olstow
Position: Director/electrician
Phone: 021 387 9415
Email: derek@quarneth.co.nz
Location: Ravenmoor
As for colors the the blue color in the logo is preferred, i also don't mind a black background option.
Target Market(s)
High end residential and commercial
Industry/Entity Type
Electrician
Contact Information for Business Card
Name: Derek Olstow Position: Director/Electrician Phone: 021 387 9415, Email: derek@quarneth.co.nz, Location: Ravenmoor

```html
<!DOCTYPE html>
<html lang="en">
<head>
<meta charset="utf-8">
<title>Quarneth Ltd — Business Card</title>
<link rel="stylesheet" href="https://fonts.googleapis.com/css2?family=Michroma&family=Montserrat:wght@600;700&family=Arimo:wght@400&display=swap">
<style>
  :root {
    --stage: #0e0e0e;
    --slate-light: #5a5e62;
    --slate-dark: #45484b;
    --blue-deep: #0d4ea6;
    --blue-mid: #0a5fa8;
    --blue-bright: #1f7fd0;
    --paper: #e9e8e9;
    --ink: #2a2b2d;
    --ink-grey: #55585c;
    --white: #f4f4f4;
  }
  * { box-sizing: border-box; margin: 0; padding: 0; }
  html, body {
    width: 1200px; height: 1000px; overflow: hidden;
    background: var(--stage);
  }
  .card {
    position: absolute; left: 207px; width: 786px; height: 447px;
    border-radius: 18px; overflow: hidden;
  }
  .card--front {
    top: 40px;
    background: linear-gradient(200deg, var(--slate-light) 0%, var(--slate-dark) 100%);
  }
  .card--back { top: 514px; background: var(--paper); }

  .front-band { position: absolute; inset: 0; width: 100%; height: 100%; }

  .wordmark {
    font-family: "Montserrat", sans-serif; font-weight: 700;
    letter-spacing: 1px; line-height: 1; white-space: nowrap;
  }
  .tagline {
    font-family: "Montserrat", sans-serif; font-weight: 700;
    letter-spacing: 0.8px; line-height: 1; white-space: nowrap;
  }
  .front-brand { position: absolute; right: 128px; top: 198px; text-align: right; }
  .front-brand .wordmark { color: var(--white); font-size: 44px; }
  .front-brand .tagline { color: var(--white); font-size: 15.5px; margin-top: 12px; }

  .back-brand { position: absolute; right: 453px; top: 210px; text-align: right; }
  .back-brand .wordmark { color: var(--ink-grey); font-size: 38px; }
  .back-brand .tagline { color: var(--ink-grey); font-size: 13px; margin-top: 10px; }

  .divider {
    position: absolute; left: 375px; top: 144px; width: 2px; height: 188px;
    background: var(--blue-mid);
  }
  .details { position: absolute; left: 415px; top: 140px; width: 318px; }
  .person-name {
    font-family: "Michroma", sans-serif; font-weight: 400; font-size: 26.5px; line-height: 1;
    letter-spacing: 0.5px; white-space: nowrap;
  }
  .person-name .first { color: var(--blue-deep); }
  .person-name .last { color: var(--blue-bright); }
  .person-role {
    font-family: "Montserrat", sans-serif; font-weight: 600; font-size: 20.5px;
    color: var(--ink); margin-top: 13px; letter-spacing: 0.5px; white-space: nowrap;
  }
  .rule { height: 1.5px; background: var(--blue-mid); margin-top: 18px; }
  .contact-list { list-style: none; margin-top: 18px; }
  .contact-list li {
    display: flex; align-items: center; gap: 10px; height: 32.5px;
    font-family: "Arimo", sans-serif; font-size: 21px; color: var(--ink);
  }
  .contact-list svg { width: 22px; height: 22px; fill: var(--blue-mid); flex: none; }
</style>
</head>
<body>

<section class="card card--front" aria-label="Card front">
  <svg class="front-band" viewBox="0 0 786 447" aria-hidden="true">
    <defs>
      <linearGradient id="bandBlue" x1="0" x2="1">
        <stop offset="0" stop-color="#0a5e9c"/>
        <stop offset="1" stop-color="#0f48a0"/>
      </linearGradient>
    </defs>
    <polygon points="0,0 232,0 116,447 0,447" fill="url(#bandBlue)"/>
    <polygon points="232,0 362,0 128,447 116,447" fill="#ececec"/>
  </svg>
  <div class="front-brand">
    <div class="wordmark">QUARNETH</div>
    <div class="tagline">WIRED FOR EXCELLENCE</div>
  </div>
</section>

<section class="card card--back" aria-label="Card back">
  <div class="back-brand">
    <div class="wordmark">QUARNETH</div>
    <div class="tagline">WIRED FOR EXCELLENCE</div>
  </div>
  <div class="divider"></div>
  <div class="details">
    <h1 class="person-name"><span class="first">DEREK</span> <span class="last">OLSTOW</span></h1>
    <p class="person-role">DIRECTOR / ELECTRICIAN</p>
    <div class="rule"></div>
    <ul class="contact-list">
      <li>
        <svg viewBox="0 0 24 24" aria-hidden="true"><path d="M3 4h6v17H3zM10 6h11v15H10zm2 2v3h7V8zm0 5v2h2v-2zm3 0v2h2v-2zm3 0v2h1v-2zm-6 3v2h2v-2zm3 0v2h2v-2zm3 0v2h1v-2zM5 2h2v2H5z"/></svg>
        <span>021 387 9415</span>
      </li>
      <li>
        <svg viewBox="0 0 24 24" aria-hidden="true"><path d="M22 3 2 11l6 2.5L19 6l-9 9v6l3.5-4.5L18 19z"/></svg>
        <span>derek@quarneth.co.nz</span>
      </li>
      <li>
        <svg viewBox="0 0 24 24" aria-hidden="true"><path d="M12 2a7 7 0 0 0-7 7c0 5 7 13 7 13s7-8 7-13a7 7 0 0 0-7-7zm0 9.5A2.5 2.5 0 1 1 12 6.5a2.5 2.5 0 0 1 0 5z"/></svg>
        <span>Ravenmoor</span>
      </li>
    </ul>
  </div>
</section>

</body>
</html>
```